Business Card Design Project

Hello,

We need a business card, which will be presented the our company Studio Lomarek and its brand Clipharbor.
Studio Lomarek is a video production company.
Stock video footage Clipharbor is a trademark of Studio Lomarek.
We need a designer that will set both the logo and contacts on the card. Print will be executed on a single page, it will use a translucent paper.

Contacts:

Andrej Zupevec
Founder and CEO

Studio Lomarek d.o.o., Cesta pod Lipami 14, 8000 Novo mesto, Slovenia
T: +386 599 81 306, M: +386 41 902 153
andrej@lomarek-example.si, www.lomarek-example.si
info@clipharbor-example.com, www.clipharbor-example.com

In the attachment are located both logo!

Thanks in advance,

Andrej

```html
<!DOCTYPE html>
<html lang="en">
<head>
<meta charset="utf-8">
<title>Studio Lomarek – Business Card</title>
<link rel="stylesheet" href="https://fonts.googleapis.com/css2?family=Open+Sans:wght@400;600;700&display=swap">
<style>
  :root {
    --page: #e9e4dc;
    --card: #f3ece0;
    --ink: #1d1d1d;
    --grey: #6f6f6f;
    --orange: #ee7b2c;
    --blue: #1c9ad8;
    --blue-light: #1ca9e6;
    --blue-deep: #0c72bd;
    --chevron: #1d3a5c;
    --white: #ffffff;
  }
  * { margin: 0; padding: 0; box-sizing: border-box; }
  html, body {
    width: 1200px; height: 738px; overflow: hidden;
    background: var(--page);
    font-family: "Open Sans", sans-serif;
    color: var(--ink);
  }
  .card {
    position: absolute; left: 190px; top: 138px;
    width: 818px; height: 470px;
    background: var(--card);
    box-shadow: 0 4px 14px rgba(0,0,0,0.18);
    overflow: hidden;
  }
  .studio-mark {
    position: absolute; left: 48px; top: 88px;
    display: flex; align-items: center; gap: 14px;
    font-size: 38px; font-weight: 400; color: var(--grey);
    letter-spacing: 1px;
  }
  .studio-mark .dot {
    width: 26px; height: 26px; border-radius: 50%; background: var(--grey);
  }
  .address {
    position: absolute; left: 46px; top: 182px;
    font-size: 17px; line-height: 29px; white-space: nowrap;
  }
  .address .label { color: var(--orange); font-weight: 600; }
  .studio-web {
    position: absolute; right: 58px; top: 252px;
    font-size: 17px; font-weight: 700; letter-spacing: 3.5px;
  }
  .divider {
    position: absolute; left: 0; right: 0; top: 286px;
    height: 2px; background: var(--orange);
  }
  .brand-contacts {
    position: absolute; left: 48px; top: 322px;
    font-size: 17px; line-height: 27px;
  }
  .brand-mark {
    position: absolute; right: 58px; top: 314px; text-align: right;
  }
  .brand-mark .name {
    font-size: 34px; font-weight: 700; color: var(--blue); line-height: 1;
  }
  .brand-mark .tagline {
    margin-top: 6px; font-size: 15px; letter-spacing: 0.5px; color: var(--ink);
  }
  .title-band {
    position: absolute; left: 0; top: 396px; width: 818px; height: 47px;
  }
  .title-band svg { position: absolute; inset: 0; }
  .person-name {
    position: absolute; left: 46px; top: 0; line-height: 47px;
    font-size: 28px; font-weight: 600; color: var(--white); letter-spacing: 0.5px;
  }
  .person-role {
    position: absolute; right: 56px; top: 0; line-height: 47px;
    font-size: 19px; color: var(--white);
  }
  .band-blue-start { stop-color: var(--blue-light); }
  .band-blue-end { stop-color: var(--blue-deep); }
</style>
</head>
<body>
  <section class="card">
    <div class="studio-mark"><span class="dot"></span>Studio Lomarek</div>

    <p class="address">
      Studio Lomarek d.o.o., Cesta pod Lipami 14, 8000 Novo Mesto, Slovenia<br>
      <span class="label">T:</span> +386 599 81 306, <span class="label">M:</span> +386 41 902 153 &nbsp;&nbsp;<span class="label">E:</span> andrej@lomarek-example.si
    </p>
    <p class="studio-web">www.lomarek-example.si</p>

    <div class="divider"></div>

    <p class="brand-contacts">
      info@clipharbor-example.com<br>
      www.clipharbor-example.com
    </p>

    <div class="brand-mark">
      <div class="name">Clipharbor</div>
      <div class="tagline">SIMPLE STOCK FOOTAGE</div>
    </div>

    <div class="title-band">
      <svg width="818" height="47" viewBox="0 0 818 47" aria-hidden="true">
        <defs>
          <linearGradient id="blueBand" x1="0" x2="1" y1="0" y2="0">
            <stop offset="0" class="band-blue-start"/>
            <stop offset="1" class="band-blue-end"/>
          </linearGradient>
        </defs>
        <rect x="400" y="0" width="418" height="47" fill="url(#blueBand)"/>
        <polygon points="408,0 432,23.5 408,47 422,47 446,23.5 422,0" fill="#1d3a5c"/>
        <polygon points="0,0 410,0 434,23.5 410,47 0,47" fill="#ee7b2c"/>
        <polygon points="410,0 416,0 440,23.5 416,47 410,47 434,23.5" fill="#ffffff"/>
      </svg>
      <span class="person-name">ANDREJ ZUPEVEC</span>
      <span class="person-role">Founder and CEO</span>
    </div>
  </section>
</body>
</html>
```